Business Card Design Project

I am looking for a classy business card design for a product design consultancy. We specialize in Product Design, Prototyping, and Manufacturing Consulting. Products that we design range from consumer electronics to household products all the way to sporting goods. We are based in Arizona and called "Heron Design Works." We like to have fun and goof off as much as we like to create new products. We are young and energetic so we would like our business cards to reflect that. We already have a logo that we would like to implement into the card design. A plain rectangular business card is boring so feel free to get creative, but please, no avocado shaped cards (it's far too literal). Also feel free to play around with textured card stocks or plastic. The final design that we choose will pay attention to all of the little details. Our cards will need to be 2 sided. We're giving you guys free reign to design as you would like. Please have fun with this, it will reflect in our business card.

Thanks guys,
Heron Design Works Team

Industry/Entity Type

Electronics

Requirements
Must have
• We would like to have a spot UV coating somewhere on the business card design if possible.
Nice to have
• Let's see some designs with custom shapes rather than typical rectangular business cards but please no avocado shaped cards, thanks. Also play around with textured card socks.

```html
<!DOCTYPE html>
<html lang="en">
<head>
<meta charset="utf-8">
<title>Heron Design Works – Business Card</title>
<link rel="stylesheet" href="https://fonts.googleapis.com/css2?family=Mulish:ital,wght@0,400;0,600;1,400&display=swap">
<style>
  :root {
    --backdrop: #e6e6e4;
    --card-white: #f7f7f6;
    --leaf-green: #8cb826;
    --ink-white: #ffffff;
    --ink-grey: #9a9a9a;
    --card-shadow: rgba(0, 0, 0, 0.18);
  }
  * { box-sizing: border-box; margin: 0; padding: 0; }
  html, body {
    width: 1200px;
    height: 900px;
    overflow: hidden;
  }
  body {
    background: var(--backdrop);
    font-family: "Mulish", sans-serif;
    position: relative;
  }
  .card {
    position: absolute;
    left: 290px;
    width: 620px;
    height: 230px;
    border-radius: 42px;
    box-shadow: 0 10px 24px var(--card-shadow);
  }
  .card--front {
    top: 150px;
    background: var(--card-white);
    display: flex;
    align-items: center;
    padding-left: 64px;
    gap: 22px;
  }
  .brand-dot {
    width: 64px;
    height: 64px;
    border-radius: 50%;
    background: var(--leaf-green);
    flex: none;
  }
  .brand-name {
    color: var(--leaf-green);
    font-weight: 600;
    font-size: 44px;
    letter-spacing: 0.5px;
    white-space: nowrap;
  }
  .card--back {
    top: 510px;
    background: var(--leaf-green);
    color: var(--ink-white);
  }
  .contact {
    position: absolute;
    left: 70px;
    top: 34px;
  }
  .contact__name {
    font-size: 28px;
    font-weight: 400;
    letter-spacing: 0.5px;
    text-transform: uppercase;
    line-height: 1.1;
  }
  .contact__role {
    font-size: 18px;
    font-style: italic;
    margin-left: -8px;
    margin-bottom: 12px;
  }
  .contact__line {
    font-size: 18px;
    line-height: 1.35;
  }
  .contact__label {
    display: inline-block;
    width: 28px;
  }
  .contact__web {
    margin-top: 8px;
    font-size: 18px;
  }
  .back-mark {
    position: absolute;
    right: 56px;
    top: 78px;
    width: 74px;
    height: 74px;
  }
</style>
</head>
<body>
  <section class="card card--front">
    <span class="brand-dot"></span>
    <span class="brand-name">Heron Design Works</span>
  </section>

  <section class="card card--back">
    <div class="contact">
      <p class="contact__name">Dylan Marsh</p>
      <p class="contact__role">President</p>
      <p class="contact__line"><span class="contact__label">T</span>480.555.0142</p>
      <p class="contact__line"><span class="contact__label">M</span>602.555.0187</p>
      <p class="contact__line">dylan@herondesignworks.com</p>
      <p class="contact__web">www.herondesignworks.com</p>
    </div>
    <svg class="back-mark" viewBox="0 0 74 74" aria-hidden="true">
      <circle cx="37" cy="37" r="37" fill="#ffffff"/>
    </svg>
  </section>
</body>
</html>
```